Ridge 4 Harbor Networkss LLC. "Minding every Connection So you never need to" or somthing similar.

We need a logo design that represents our Technology company. We supply Restaurant Point of Sales Systems, Business Networks, and on going Network Administration. The business card should be in a color that stands out red and gray, orange and gray or a combination of all red, grey, orange and black/white. We are open to the designers ideas.

We would like a file where we can edited the information for different employees so we can have our local card printer reproduce them.
On front:
Marek Lindqvist
Ridge 4 Harbor Networks LLC.
Oregon, New Hampshire, Utah
marek@r4hnet.example
866.203.5194
707.418.3659

On Back logos of our partners: (included in uploads)
Put text at bottom " And Many more... "

Target Market(s)

Point of sales, law offices, medical networks, and small businesses.

Industry/Entity Type

Business

Contact Information for Business Card

Front should have logo Phone Numbers. Phone: 866-203-5194, Local number: need to be editable .

Logo Text

Not sure if it should be "R4H" or " Ridge 4 Harbor Networks LLC" or a shaped logo. Open to suggentions.

Font styles to use
Serif

Colors
ec1f27
757575
f37122
ffffff

Requirements
Must have
• editable file preferably as .ai or .pdf. that retains all original data. resolution should be at least 325 dpi.
Nice to have
• I have a hand drawn logo attachment. Can someone create this and clean it up? Note there are three stars. Add a additional star to sothern California.

```html
<!DOCTYPE html>
<html lang="en">
<head>
<meta charset="utf-8">
<title>Ridge 4 Harbor Networks LLC – Business Cards</title>
<link rel="stylesheet" href="https://fonts.googleapis.com/css2?family=Orbitron:wght@700&family=Open+Sans:wght@400;700&display=swap">
<style>
  :root {
    --brand-red: #ec1f27;
    --brand-red-deep: #b5121a;
    --brand-red-shade: #d0161e;
    --ink-black: #0c0c0c;
    --card-white: #f7f7f6;
    --page-bg: #e9e8e6;
    --text-light: #ffffff;
  }
  * { box-sizing: border-box; margin: 0; padding: 0; }
  html, body { width: 1200px; height: 680px; overflow: hidden; }
  body {
    background: var(--page-bg);
    display: flex;
    align-items: center;
    justify-content: center;
    gap: 40px;
    font-family: "Open Sans", Arial, sans-serif;
  }
  .card {
    position: relative;
    width: 540px;
    height: 309px;
    background: var(--card-white);
    overflow: hidden;
    box-shadow: 0 2px 6px rgba(0,0,0,0.12);
  }
  .card-shapes { position: absolute; inset: 0; width: 100%; height: 100%; }

  .company-name {
    position: absolute;
    font-family: "Open Sans", Arial, sans-serif;
    font-weight: 700;
    color: var(--brand-red);
    text-align: center;
    line-height: 1.15;
  }
  .card--logo .company-name { left: 150px; top: 124px; width: 300px; font-size: 25px; }
  .card--contact .company-name { left: 30px; top: 156px; width: 250px; font-size: 19px; }

  .logo-phone {
    position: absolute;
    right: 14px;
    top: 180px;
    display: flex;
    align-items: center;
    gap: 4px;
    color: var(--brand-red);
    font-size: 11.5px;
  }
  .icon-badge {
    width: 13px; height: 13px;
    background: var(--brand-red);
    display: inline-flex; align-items: center; justify-content: center;
    flex-shrink: 0;
  }
  .icon-badge svg { width: 9px; height: 9px; fill: var(--text-light); }

  .employee-name {
    position: absolute;
    left: 340px; top: 57px;
    font-family: "Orbitron", "Arial Black", sans-serif;
    font-weight: 700;
    font-size: 18px;
    color: var(--brand-red);
    white-space: nowrap;
  }
  .contact-list {
    position: absolute;
    left: 372px; top: 122px;
    list-style: none;
    color: var(--text-light);
    font-size: 12px;
    line-height: 1.2;
  }
  .contact-item { display: flex; gap: 7px; margin-bottom: 9px; align-items: flex-start; }
  .contact-item .icon-badge { margin-top: 1px; }
</style>
</head>
<body>

  <section class="card card--logo" aria-label="Business card, logo side">
    <svg class="card-shapes" viewBox="0 0 540 309" aria-hidden="true">
      <polygon points="0,0 220,0 0,72" fill="var(--brand-red)"/>
      <polygon points="0,48 220,0 0,118" fill="var(--brand-red-shade)"/>
      <polygon points="0,92 220,0 0,118" fill="var(--brand-red-deep)"/>
      <line x1="0" y1="196" x2="400" y2="196" stroke="var(--brand-red)" stroke-width="1.6"/>
    </svg>
    <div class="company-name">Ridge 4 Harbor Networks LLC</div>
    <div class="logo-phone">
      <span class="icon-badge"><svg viewBox="0 0 10 10"><path d="M2 1l2 2-1 1c.5 1.2 1.4 2.1 2.6 2.6l1-1 2 2-1.2 1.3C4.6 8.8 1.2 5.4 1 1.6z"/></svg></span>
      <span>866-203-5194</span>
    </div>
  </section>

  <section class="card card--contact" aria-label="Business card, contact side">
    <svg class="card-shapes" viewBox="0 0 540 309" aria-hidden="true">
      <polygon points="250,52 330,52 348,196 440,309 392,309 300,190" fill="var(--brand-red)"/>
      <polygon points="300,190 348,196 440,309 392,309" fill="var(--brand-red-deep)"/>
      <polygon points="322,0 540,0 540,309 440,309 348,196 330,52" fill="var(--ink-black)"/>
      <polygon points="327,44 540,44 540,98 333,98" fill="var(--card-white)"/>
      <g stroke="var(--brand-red)" stroke-width="1.6" fill="none">
        <line x1="340" y1="129" x2="370" y2="129"/>
        <line x1="344" y1="163" x2="370" y2="163"/>
        <line x1="350" y1="188" x2="370" y2="188"/>
      </g>
    </svg>
    <div class="company-name">Ridge 4 Harbor Networks LLC</div>
    <div class="employee-name">Marek Lindqvist</div>
    <ul class="contact-list">
      <li class="contact-item">
        <span class="icon-badge"><svg viewBox="0 0 10 10"><path d="M2 1l2 2-1 1c.5 1.2 1.4 2.1 2.6 2.6l1-1 2 2-1.2 1.3C4.6 8.8 1.2 5.4 1 1.6z"/></svg></span>
        <span>866.203.5194<br>707.418.3659</span>
      </li>
      <li class="contact-item">
        <span class="icon-badge"><svg viewBox="0 0 10 10"><path d="M1 2h8v6H1z M1 2l4 3 4-3" fill="none" stroke="#fff" stroke-width="1"/></svg></span>
        <span>marek@r4hnet.example</span>
      </li>
      <li class="contact-item">
        <span class="icon-badge"><svg viewBox="0 0 10 10"><path d="M5 .8C3.3.8 2 2.1 2 3.7 2 6 5 9.2 5 9.2S8 6 8 3.7C8 2.1 6.7.8 5 .8zm0 4.1a1.2 1.2 0 110-2.4 1.2 1.2 0 010 2.4z"/></svg></span>
        <span>Oregon, New Hampshire,<br>Utah</span>
      </li>
    </ul>
  </section>

</body>
</html>
```